Kora Mall

I need a powerful power point presentation to translate my executive summary into words and graphics, utilizing all the resources necessary to produce a 12-14 page Powerpoint pitch book in order to convince potential investors of my business idea. The concept behind the Mall is to develop a number of unique standalone community malls, targeting the under-served residential communities in -.
The Mall will be built around family and their younger generation audience, creating a unique atmosphere that is conducive to making the MALL a regular local destination for the residents.
Each community mall will be remarkably designed around light, nature and music in a way not done before. The Mall will bring essential goods and services to each community that has been neglected by the large mall operators. [PLEASE CHECK ATTACHMENT OF THE PITCH BOOK WHICH I DREW OUT TO GIVE YOU AN IDEA OF THE ESSENTIAL PAGES]

I have added the LOGO of the project to give you an idea of how to choose your color schemes for the powerpoint presentation.

Reason: Interesting submissions. Need more time to assess with designers..

Dear all,

I am on the verge of finalizing with a designer. Anyone who has or about to start working on a design, I would ask you not to in order not to waste your time. Many thanks for your interests..

Target Market(s)

Mid to upper market. Colours should be greys, blacks, browns and earthy.. This is a mall project in the middle of the desert.

Industry/Entity Type

Residential

Requirements
Must have
• Since this is a real estate project, there must be maps of the area surrounding the project, the actual location using google maps, nice soft rounded/friendly graphics showing returns to investors and cost of project, snap shots of mall designs that give an idea of the design (actual designs will be given later)... Etc..
Nice to have
• Cool graphics, info graphics explaining things in a way investors can grab, especially relating to financial matters. Ha to have a good sense of continuity in the presentation..
Should not have
• too bright or fun colours... This is a serious real estate project BUT it is designed for the younger generation but for the enjoyment of all. The only bright colours will come from the logo which is under design. The logo will have an element of orange and red in it.

```html
<!DOCTYPE html>
<html lang="en">
<head>
<meta charset="utf-8">
<title>Kora Mall – Company Presentation</title>
<link href="https://fonts.googleapis.com/css2?family=Roboto:wght@300;400;700&display=swap" rel="stylesheet">
<style>
:root{
  --stage:#7b7b7e;
  --dark:#3a3a44;
  --dark-2:#5c5c66;
  --light:#ececec;
  --ink:#55555f;
  --ink-soft:#6e6e76;
  --orange:#f26a2e;
  --amber:#f7a21b;
  --white:#ffffff;
}
*{box-sizing:border-box;margin:0;padding:0}
html,body{width:1060px;height:1200px;overflow:hidden;background:var(--stage);font-family:'Roboto',Arial,sans-serif}
.deck{position:relative;width:1060px;height:1200px}
.slide{position:absolute;width:514px;height:385px;background:var(--light);overflow:hidden}
.col-a{left:12px}.col-b{left:534px}
.row-1{top:9px}.row-2{top:405px}.row-3{top:801px}
.abs{position:absolute}

/* brand name mark */
.brand{display:flex;align-items:center;gap:6px;color:var(--dark-2);font-weight:300;white-space:nowrap}
.brand .dot{border-radius:50%;background:var(--orange);flex:none}

/* cover */
.cover{background:var(--dark)}
.cover .brand{position:absolute;left:0;right:0;top:140px;justify-content:center;color:#8a8a90;font-size:64px;gap:16px}
.cover .brand .dot{width:40px;height:40px}

/* side tab */
.tab{position:absolute;left:0;width:64px;background:var(--dark)}
.tab .cap{height:18px;background:var(--dark-2)}
.tab .fold{position:absolute;right:0;bottom:0;width:0;height:0;border-left:18px solid transparent;border-bottom:18px solid var(--light)}
.tab .fold-shade{position:absolute;right:0;bottom:0;width:18px;height:18px;background:var(--dark-2);clip-path:polygon(0 100%,100% 0,0 0)}
.tab .brand{flex-direction:column;gap:3px;margin-top:14px;color:#9a9aa0;font-size:13px}
.tab .brand .dot{width:22px;height:22px}

/* title slide */
.title-main{left:75px;top:66px;font-size:64px;font-weight:300;color:var(--ink);letter-spacing:-1px;line-height:1}
.title-sub{left:76px;top:138px;font-size:31px;font-weight:300;color:var(--dark);line-height:1.14}
.title-exp{left:76px;top:232px;font-size:28px;font-weight:300;color:var(--ink-soft)}
.title-date{left:76px;top:266px;font-size:18px;font-weight:300;color:var(--ink)}

/* agenda */
.agenda-head{left:75px;top:64px;font-size:68px;font-weight:300;color:var(--ink);line-height:1}
.agenda-item{left:78px;font-size:32px;font-weight:300;color:var(--dark);line-height:1}
.agenda-item small{display:block;font-size:12px;color:var(--ink-soft);margin:3px 0 0 24px}

/* header / footer */
.header{position:absolute;left:0;top:0;width:514px;height:40px}
.header .bar{position:absolute;left:0;top:0;height:37px;background:var(--dark);color:var(--white);font-size:18px;font-weight:300;padding:8px 0 0 8px}
.header .bar em{font-style:normal;color:var(--amber)}
.header .flap{position:absolute;top:20px;width:18px;height:17px;background:var(--dark-2);clip-path:polygon(0 100%,100% 0,0 0)}
.header .brand{position:absolute;right:12px;top:6px;font-size:26px;color:var(--dark-2)}
.header .brand .dot{width:26px;height:26px}
.footer{position:absolute;left:0;bottom:0;width:514px;height:25px;background:var(--dark);display:flex;align-items:center;color:var(--white);font-size:9px}
.footer .num{width:28px;height:100%;background:var(--dark-2);display:flex;align-items:center;justify-content:center;font-weight:700;font-size:9px}
.footer .brand{color:var(--white);font-size:13px;gap:4px;margin-left:10px}
.footer .brand .dot{width:12px;height:12px}
.footer .where{margin-left:6px;font-weight:400;letter-spacing:-.2px}

/* location */
.map{left:127px;top:84px;width:349px;height:241px;border:2px solid var(--white);box-shadow:0 0 0 1px #cfcfcf;
  background:radial-gradient(circle at 75% 45%,#5f7a4e 0,#4c6440 40%,transparent 70%),linear-gradient(100deg,#8a8470 0%,#6c6a55 25%,#586b45 55%,#4f6a42 100%)}
.loc-label{right:402px;text-align:right;font-size:8.5px;color:var(--ink-soft);line-height:1.3;width:110px}
.loc-label b{display:block;font-size:11px;color:var(--dark);font-weight:700}

/* team */
.person{left:39px;width:460px;height:78px}
.person .photo{position:absolute;left:0;top:0;width:78px;height:78px;border:3px solid var(--white);box-shadow:0 0 0 1px #d0d0d0;background:linear-gradient(160deg,#8da2bd,#4c5d76)}
.person .bio{position:absolute;left:86px;top:8px;width:340px;font-size:7.6px;color:var(--ink-soft);line-height:1.4}
.person .bio h3{font-size:11.5px;color:var(--dark);font-weight:700;line-height:1.3}
.person .bio h4{font-size:8.5px;color:var(--dark);font-weight:700}

/* reporting */
.lead{width:92px;height:93px;color:var(--white);text-align:center;font-size:9px;line-height:1.3;padding-top:34px}
.lead b{display:block;font-size:9.5px}
.lead.design{left:115px;top:54px;background:var(--orange)}
.lead.ops{left:294px;top:54px;background:var(--amber)}
.lead .curl{position:absolute;right:0;bottom:0;width:18px;height:18px;background:var(--light);clip-path:polygon(100% 0,100% 100%,0 100%)}
.lead .curl::before{content:"";position:absolute;inset:0;background:rgba(0,0,0,.18);clip-path:polygon(0 100%,100% 0,0 0)}
.unit{width:80px;height:40px;background:var(--dark);color:var(--white);font-size:8.5px;text-align:center;line-height:1.25;display:flex;flex-direction:column;justify-content:center}
.unit b{font-weight:700}
.unit.right{left:404px;background:var(--dark-2)}
.unit.left{left:22px}
.link-note{font-size:8.5px;color:var(--dark)}
</style>
</head>
<body>
<main class="deck">

  <!-- Cover -->
  <section class="slide cover col-a row-1">
    <div class="brand"><span class="dot"></span>Kora Mall</div>
  </section>

  <!-- Title -->
  <section class="slide col-b row-1">
    <div class="tab" style="top:73px;height:254px">
      <div class="cap"></div>
      <div class="brand"><span class="dot"></span>kora<br>mall</div>
      <div class="fold-shade"></div>
    </div>
    <h1 class="abs title-main">KORA MALL</h1>
    <p class="abs title-sub">COMPANY PRESENTATION<br>TO CLIENT/CUSTOMER</p>
    <p class="abs title-exp">EXPERIENCE.</p>
    <p class="abs title-date">JUNE 2013</p>
  </section>

  <!-- Agenda -->
  <section class="slide col-a row-2">
    <div class="tab" style="top:64px;height:254px">
      <div class="cap"></div>
      <div class="brand"><span class="dot"></span>kora<br>mall</div>
      <div class="fold-shade"></div>
    </div>
    <h2 class="abs agenda-head">AGENDA</h2>
    <div class="abs agenda-item" style="top:142px">1.INTRODUCTION<small>About the company | Management</small></div>
    <div class="abs agenda-item" style="top:202px">2.OPPORTUNITY<small>Problem | Technology Solution</small></div>
    <div class="abs agenda-item" style="top:262px">3.BUSINESS MODEL<small>Plan | Milestones | Marketing | Sales</small></div>
  </section>

  <!-- Location -->
  <section class="slide col-b row-2">
    <header class="header">
      <div class="bar" style="width:402px">Location of First <em>Mall</em></div>
      <div class="flap" style="left:384px"></div>
      <div class="brand"><span class="dot"></span>kora mall</div>
    </header>
    <div class="abs map" role="img" aria-label="Satellite map of the area surrounding the first mall site"></div>
    <svg class="abs" style="left:0;top:0" width="514" height="385" aria-hidden="true">
      <circle cx="284" cy="211" r="36" fill="#f26a2e" fill-opacity=".55"/>
      <path d="M256 180a6 6 0 1 1 12 0c0 5-6 10-6 10s-6-5-6-10z" fill="#f7a21b" stroke="#fff" stroke-width="1"/>
      <circle cx="262" cy="180" r="2" fill="#fff"/>
      <g stroke="#f7a21b" stroke-width="1" fill="none">
        <line x1="102" y1="85" x2="102" y2="121"/>
        <line x1="102" y1="150" x2="102" y2="186"/>
        <line x1="102" y1="218" x2="102" y2="254"/>
        <g stroke-dasharray="3 2">
          <line x1="110" y1="103" x2="262" y2="172"/>
          <line x1="110" y1="168" x2="270" y2="198"/>
          <line x1="110" y1="236" x2="250" y2="228"/>
        </g>
      </g>
    </svg>
    <div class="abs loc-label" style="top:84px"><b>Location</b>Redmesa Flats,<br>DV 40210 &nbsp;113 ft N</div>
    <div class="abs loc-label" style="top:149px"><b>XYZ</b>Redmesa Flats,<br>DV 40210 &nbsp;113 ft N</div>
    <div class="abs loc-label" style="top:217px"><b>XYZ</b>Redmesa Flats,<br>DV 40210 &nbsp;113 ft N</div>
    <footer class="footer"><span class="num">4</span><span class="brand"><span class="dot"></span>kora mall</span><span class="where">| TO CLIENT/CUSTOMER</span></footer>
  </section>

  <!-- Management -->
  <section class="slide col-a row-3">
    <header class="header">
      <div class="bar" style="width:402px">Management Team <em>Background</em></div>
      <div class="flap" style="left:384px"></div>
      <div class="brand"><span class="dot"></span>kora mall</div>
    </header>
    <article class="abs person" style="top:66px">
      <div class="photo" role="img" aria-label="Portrait of the mall manager"></div>
      <div class="bio"><h3>Mall Management</h3><h4>Daniel Hartley</h4>Eleifend suspendisse, conubia cum ultricies varius praesent justo ornare suspendisse odio imperdiet ad convallis congue tincidunt erat imperdiet. Nisl sapien imperdiet egestas nunc class dis morbi nibh curabitur torquent felis a massa.</div>
    </article>
    <article class="abs person" style="top:157px">
      <div class="photo" role="img" aria-label="Portrait of the facility manager"></div>
      <div class="bio"><h3>Facility Management</h3><h4>Owen Carraway</h4>Eleifend suspendisse, conubia cum ultricies varius praesent justo ornare suspendisse odio imperdiet ad convallis congue tincidunt erat imperdiet. Nisl sapien imperdiet egestas nunc class dis morbi nibh curabitur torquent felis a massa.</div>
    </article>
    <article class="abs person" style="top:249px">
      <div class="photo" role="img" aria-label="Portrait of the mall consultant"></div>
      <div class="bio"><h3>Mall Consultant &amp; Leasing</h3><h4>Luca Penrose</h4>Eleifend suspendisse, conubia cum ultricies varius praesent justo ornare suspendisse odio imperdiet ad convallis congue tincidunt erat imperdiet. Nisl sapien imperdiet egestas nunc class dis morbi nibh curabitur torquent felis a massa.</div>
    </article>
    <footer class="footer"><span class="num">5</span><span class="brand"><span class="dot"></span>kora mall</span><span class="where">| TO CLIENT/CUSTOMER</span></footer>
  </section>

  <!-- Reporting -->
  <section class="slide col-b row-3">
    <header class="header">
      <div class="bar" style="width:402px">Reporting</div>
      <div class="flap" style="left:384px"></div>
      <div class="brand"><span class="dot"></span>kora mall</div>
    </header>
    <svg class="abs" style="left:0;top:0" width="514" height="385" aria-hidden="true">
      <g stroke="#f26a2e" stroke-width="1" stroke-dasharray="3 2">
        <line x1="209" y1="100" x2="292" y2="100"/>
        <line x1="388" y1="100" x2="470" y2="100"/>
      </g>
      <g stroke="#55555f" stroke-width="1" fill="none">
        <line x1="164" y1="150" x2="164" y2="326"/>
        <line x1="102" y1="182" x2="164" y2="182"/>
        <line x1="102" y1="230" x2="164" y2="230"/>
        <line x1="102" y1="278" x2="164" y2="278"/>
        <line x1="102" y1="326" x2="164" y2="326"/>
        <line x1="343" y1="150" x2="343" y2="326"/>
        <line x1="343" y1="182" x2="404" y2="182"/>
        <line x1="343" y1="230" x2="404" y2="230"/>
        <line x1="343" y1="278" x2="404" y2="278"/>
        <line x1="343" y1="326" x2="404" y2="326"/>
      </g>
      <path d="M161 154l3-5 3 5z M340 154l3-5 3 5z" fill="#55555f"/>
    </svg>
    <div class="abs lead design"><b>PH. MD</b>Design &amp; Concept<br>Development<span class="curl"></span></div>
    <div class="abs lead ops"><b>GM. MD</b>Financial Operations<span class="curl"></span></div>
    <span class="abs link-note" style="left:210px;top:88px">Contract Negotiation</span>
    <span class="abs link-note" style="left:390px;top:88px">Negotiation % Local ?</span>
    <div class="abs unit left" style="top:162px"><b>DESIGN</b>RKL</div>
    <div class="abs unit left" style="top:210px"><b>Mall Consulting</b>&amp; Leasing</div>
    <div class="abs unit left" style="top:258px"><b>Facility</b>Management</div>
    <div class="abs unit left" style="top:306px"><b>Mall</b>Management</div>
    <div class="abs unit right" style="top:162px"><b>Financial</b>Director</div>
    <div class="abs unit right" style="top:210px"><b>Engineers</b></div>
    <div class="abs unit right" style="top:258px"><b>Project Mgt</b>RKL</div>
    <div class="abs unit right" style="top:306px"></div>
    <footer class="footer"><span class="num">6</span><span class="brand"><span class="dot"></span>kora mall</span><span class="where">| TO CLIENT/CUSTOMER</span></footer>
  </section>

</main>
</body>
</html>
```